Author needs design for self-help relationship book

I need a book cover design for a self-help handbook on relationships called 'Where Partners Find Calm Harbours - Letters From Quiet Mornings". The design should appeal in the main to young couples anywhere in the world.

```html
<!DOCTYPE html>
<html lang="en">
<head>
<meta charset="utf-8">
<title>Where Partners Find Calm Harbours – Book Cover</title>
<link rel="stylesheet" href="https://fonts.googleapis.com/css2?family=Bebas+Neue&family=Jost:wght@500;600&display=swap">
<style>
  :root {
    --cover-teal: #10a9a5;
    --heart-red: #e8141a;
    --paper-white: #ffffff;
    --ink-black: #1a1a1a;
  }
  html, body {
    margin: 0;
    padding: 0;
    overflow: hidden;
    background: var(--cover-teal);
  }
  .cover {
    position: relative;
    width: 800px;
    height: 1200px;
    overflow: hidden;
    background: var(--cover-teal);
  }
  .author-name {
    position: absolute;
    top: 64px;
    left: 0;
    width: 100%;
    margin: 0;
    text-align: center;
    font-family: "Jost", sans-serif;
    font-weight: 600;
    font-size: 30px;
    letter-spacing: 0.38em;
    padding-left: 0.38em;
    color: var(--paper-white);
  }
  .cover-illustration {
    position: absolute;
    left: 256px;
    top: 176px;
    width: 296px;
    height: 520px;
    border-radius: 148px 148px 12px 12px;
    background: linear-gradient(180deg, var(--heart-red) 0%, var(--heart-red) 38%, var(--paper-white) 62%, var(--ink-black) 100%);
    opacity: 0.9;
  }
  .title-block {
    position: absolute;
    left: 0;
    top: 0;
    width: 800px;
    height: 1200px;
  }
  .title-line {
    font-family: "Bebas Neue", sans-serif;
    fill: var(--paper-white);
  }
  .subtitle {
    position: absolute;
    top: 1096px;
    left: 0;
    width: 100%;
    margin: 0;
    text-align: center;
    font-family: "Jost", sans-serif;
    font-weight: 600;
    font-size: 23px;
    letter-spacing: 0.32em;
    padding-left: 0.32em;
    color: var(--heart-red);
  }
</style>
</head>
<body>
  <main class="cover">
    <p class="author-name">AUTHOR NAME</p>

    <div class="cover-illustration" role="img" aria-label="Illustration of a couple sharing a red umbrella beneath a shower of small red hearts"></div>

    <svg class="title-block" viewBox="0 0 800 1200" width="800" height="1200" aria-labelledby="book-title">
      <title id="book-title">Where Partners Find Calm Harbours</title>
      <text class="title-line" x="76" y="836" font-size="98" textLength="644" lengthAdjust="spacing">WHERE PARTNERS</text>
      <text class="title-line" x="76" y="904" font-size="60" textLength="644" lengthAdjust="spacing">FIND CALM</text>
      <text class="title-line" x="76" y="1048" font-size="162" textLength="644" lengthAdjust="spacing">HARBOURS</text>
    </svg>

    <p class="subtitle">LETTERS FROM QUIET MORNINGS</p>
  </main>
</body>
</html>
```